Business Card Design for Flood Rescue 360 - Property Restoration Professionals

I need a business card designed for Flood Rescue 360. We are a full-service property restoration solution. Providing water, fire, smoke & storm restoration as well as mold remediation and full remodel or reconstruction to homes and businesses across Dallas-Fort Worth, TX.
Target Market(s)
home and business owners with insurance covered property damage from water, fire or storm related damage
Industry/Entity Type
property restoration
Contact Information for Business Card
Marcus Pellow General Manager Cell: 214-555-0193 Office: 469-555-0148 email: Marcus@FloodRescue360.example services: Water, Fire, Mold, Reconstruction Tagline: Urgency for Your Water Emergency!
Look and feel
Each slider illustrates characteristics of the customer's brand and the style your logo design should communicate.

```html
<!DOCTYPE html>
<html lang="en">
<head>
<meta charset="utf-8">
<title>Flood Rescue 360 – Business Card</title>
<link href="https://fonts.googleapis.com/css2?family=Arimo:wght@400;700&family=Montserrat:wght@400;800&display=swap" rel="stylesheet">
<style>
  :root {
    --bg: #d3d6d7;
    --paper: #f7f8f8;
    --brand-blue: #1ba6df;
    --brand-blue-deep: #1690c4;
    --charcoal: #3d4041;
    --ink: #3a3c3d;
    --white: #ffffff;
  }
  * { box-sizing: border-box; margin: 0; padding: 0; }
  html, body { width: 1200px; height: 829px; overflow: hidden; }
  body {
    background: var(--bg);
    font-family: "Arimo", Arial, sans-serif;
    display: flex;
    align-items: center;
    justify-content: center;
    gap: 48px;
  }
  .card {
    position: relative;
    width: 520px;
    height: 297px;
    overflow: hidden;
    box-shadow: 0 6px 18px rgba(0,0,0,.18);
  }

  /* Front */
  .card--front { background: var(--paper); }
  .contact {
    position: absolute;
    left: 34px;
    top: 56px;
    color: var(--ink);
  }
  .contact__name {
    font-weight: 700;
    font-size: 22px;
    letter-spacing: .3px;
    color: var(--brand-blue);
    text-transform: uppercase;
  }
  .contact__title { font-size: 14px; margin-top: 2px; }
  .contact__list { list-style: none; margin-top: 18px; font-size: 13.5px; line-height: 22px; }
  .contact__list li { display: flex; align-items: center; gap: 8px; }
  .contact__list svg { width: 11px; height: 11px; fill: var(--brand-blue); flex: none; }
  .brand-mark {
    position: absolute;
    right: -28px;
    top: 70px;
    width: 250px;
    height: 250px;
    border-radius: 50%;
    border: 20px solid var(--charcoal);
    display: flex;
    align-items: center;
    justify-content: center;
  }
  .brand-mark__name {
    font-family: "Montserrat", Arial, sans-serif;
    font-weight: 800;
    font-size: 26px;
    line-height: 1.1;
    color: var(--brand-blue);
    text-align: center;
    width: 160px;
  }

  /* Back */
  .card--back { background: var(--brand-blue); color: var(--white); }
  .back__logo {
    position: absolute;
    left: 0; right: 0;
    top: 58px;
    text-align: center;
    font-family: "Montserrat", Arial, sans-serif;
    font-weight: 800;
    font-size: 44px;
    line-height: 1;
    text-transform: uppercase;
    letter-spacing: -.5px;
  }
  .back__services {
    position: absolute;
    left: 0; right: 0;
    top: 150px;
    text-align: center;
    font-family: "Montserrat", Arial, sans-serif;
    font-size: 15px;
    letter-spacing: 1.5px;
  }
  .back__band {
    position: absolute;
    left: 0; right: 0;
    top: 190px;
    height: 30px;
    background: var(--charcoal);
    display: flex;
    align-items: center;
    justify-content: center;
  }
  .back__tagline {
    font-family: "Montserrat", Arial, sans-serif;
    font-weight: 800;
    font-size: 13px;
    letter-spacing: .6px;
    color: var(--brand-blue);
  }
</style>
</head>
<body>
  <section class="card card--front">
    <div class="contact">
      <h1 class="contact__name">Marcus Pellow</h1>
      <p class="contact__title">General Manager</p>
      <ul class="contact__list">
        <li><svg viewBox="0 0 12 12"><path d="M1 4c0-2 2-3 5-3s5 1 5 3l-2 1-1-2H4L3 5zM2 6h8v5H2z"/></svg>469-555-0148</li>
        <li><svg viewBox="0 0 12 12"><path d="M3 0h6v12H3zM4 1v8h4V1z"/></svg>214-555-0193</li>
        <li><svg viewBox="0 0 12 12"><path d="M0 2h12v8H0zM1 3l5 4 5-4z"/></svg>Marcus@FloodRescue360.example</li>
        <li><svg viewBox="0 0 12 12"><circle cx="6" cy="6" r="6"/></svg>www.FloodRescue360.example</li>
      </ul>
    </div>
    <div class="brand-mark">
      <span class="brand-mark__name">Flood Rescue 360</span>
    </div>
  </section>

  <section class="card card--back">
    <div class="back__logo">Flood Rescue 360</div>
    <p class="back__services">Water • Fire • Mold • Reconstruction</p>
    <div class="back__band">
      <p class="back__tagline">Urgency for Your Water Emergency!</p>
    </div>
  </section>
</body>
</html>
```